New Website for ReBranded Company - CrewBeacon

We have a successful company and website currently but it is a little dated. We have re-branded the company from Harbor Signal Networks to CrewBeacon and have a new logo for the new name. We are looking to build a newer fresher website with the new name. I will need a concept of the home page and one inside page. You can see our current site at https://www.harborsignalnetworks.example and the new site will be https://www.crewbeacon.example .

I also really like the https://www.pathlantern.example/ website. I like ledgerkite.example website. I like the https://skillorbit.example/ website.

See the attached document for layout and some text to use. Use the pictures I attached as opposed to pictures from the old site as much as you can.

Target Market(s)

Business

Industry/Entity Type

Software Service

Number of Pages Required

2 page

Font styles to use
Sans Serif

Requirements
Must have
• Use the colors from my logo. Professional but modern. We want people to feel like our product makes their staff feel safer at work.
Should not have
• Don't use any red or orange (no stop colors).

```html
<!DOCTYPE html>
<html lang="en">
<head>
<meta charset="utf-8">
<title>CrewBeacon</title>
<link href="https://fonts.googleapis.com/css2?family=Poppins:wght@400;500;600;700;800&display=swap" rel="stylesheet">
<style>
:root{
  --blue:#3a8fd6;
  --green:#7bb83a;
  --ink:#333333;
  --ink-soft:#555555;
  --grey-title:#4a4a4a;
  --white:#ffffff;
}
*{box-sizing:border-box;margin:0;padding:0}
html,body{width:1200px;height:3778px;overflow:hidden;background:var(--white)}
body{font-family:'Poppins',sans-serif;color:var(--ink);position:relative}
.abs{position:absolute}
a{color:inherit;text-decoration:none}

/* header */
.site-header{position:absolute;left:0;top:0;width:1200px;height:75px;background:var(--white)}
.brand{position:absolute;left:150px;top:16px;display:flex;align-items:center;gap:12px}
.brand-dot{width:42px;height:42px;border-radius:50%;background:var(--blue)}
.brand-name{font-size:30px;font-weight:600;color:var(--blue);line-height:1}
.nav{position:absolute;top:28px;font-size:14px;font-weight:500;color:var(--ink-soft)}
.btn{display:flex;align-items:center;justify-content:center;border-radius:30px;color:var(--white);font-weight:700;background:var(--blue)}
.btn-login{position:absolute;left:937px;top:15px;width:113px;height:45px;background:var(--green);font-size:15px}

/* hero */
.hero{position:absolute;left:0;top:75px;width:1200px;height:525px;background:linear-gradient(120deg,#4b4d4a 0%,#2f3130 45%,#565a55 100%)}
.hero-title{position:absolute;left:150px;top:140px;font-size:39px;font-weight:800;color:var(--white);line-height:52px;letter-spacing:-0.5px}
.accent{color:var(--blue)}
.hero-sub{position:absolute;left:150px;top:267px;font-size:14.5px;color:var(--white);font-weight:500}
.btn-hero{position:absolute;left:150px;top:320px;width:208px;height:50px;font-size:17px}

.features{position:absolute;left:150px;top:520px;width:900px;height:200px;background:var(--white);border-radius:8px}
.feature{position:absolute;top:35px;width:300px;text-align:center}
.feature svg{display:block;margin:0 auto 18px}
.feature p{font-size:12.5px;font-weight:600;line-height:19px;color:var(--ink)}

/* bands */
.band{position:absolute;left:0;width:1200px;text-align:center;color:var(--white)}
.band-title{font-size:39px;font-weight:800;line-height:52px;letter-spacing:-0.5px}
.band-sub{font-size:15px;font-weight:500;line-height:26px}
.problem{top:791px;height:375px;background:linear-gradient(100deg,#6b6a66 0%,#4a4a48 50%,#2e2f31 100%)}

/* why choose */
.section-title{position:absolute;left:0;width:1200px;text-align:center;font-size:37px;font-weight:800;color:var(--grey-title);letter-spacing:-0.5px}
.why{position:absolute;top:1290px;width:240px;text-align:center}
.why svg{display:block;margin:0 auto 20px}
.why h3{font-size:14px;font-weight:600;margin-bottom:16px}
.why p{font-size:11px;line-height:18px;color:var(--ink-soft)}
.opts{display:grid;grid-template-columns:1fr 1fr;text-align:left;font-size:11px;line-height:18px;color:var(--ink-soft);width:280px;margin:0 auto}

.earth{top:1582px;height:548px;background:radial-gradient(ellipse at 40% 80%,#2a3b52 0%,#121a26 55%,#080b12 100%)}
.stats{font-size:17px;font-weight:700}
.stats span.small{font-size:14px;font-weight:500;margin:0 18px}

/* start plan */
.plan-img{position:absolute}
.plan-text{position:absolute}
.plan-text h3{font-size:21px;font-weight:800;color:var(--ink);letter-spacing:-0.3px;margin-bottom:14px}
.plan-text li{list-style:none;font-size:14px;font-weight:700;color:var(--blue);line-height:30px}

/* footer */
.site-footer{position:absolute;left:0;top:3395px;width:1200px;height:383px;background:linear-gradient(120deg,#3e3e3e 0%,#333 60%,#2c2c2c 100%);color:var(--white)}
.foot-brand{position:absolute;left:150px;top:36px;display:flex;align-items:center;gap:14px}
.foot-brand .brand-dot{width:56px;height:56px}
.foot-brand .brand-name{font-size:38px}
.foot-about{position:absolute;left:150px;top:122px;width:320px;font-size:11.5px;line-height:19px;color:#e8e8e8}
.call{position:absolute;left:150px;top:222px;display:flex;align-items:center;gap:16px}
.call-label{font-size:17px;font-weight:600;text-align:center}
.call-num{font-size:19px;font-weight:700}
.foot-col{position:absolute;top:40px}
.foot-col h4{font-size:17px;font-weight:600;padding-bottom:8px;border-bottom:2px solid var(--blue);display:inline-block;width:75px;margin-bottom:14px}
.foot-col li{list-style:none;font-size:12.5px;font-weight:500;line-height:32.5px}
.foot-rule{position:absolute;left:150px;top:318px;width:900px;height:1px;background:#777}
.copyright{position:absolute;left:0;width:1200px;top:345px;text-align:center;font-size:9px;color:#ddd}
</style>
</head>
<body>

<header class="site-header">
  <div class="brand">
    <div class="brand-dot"></div>
    <div class="brand-name">CrewBeacon</div>
  </div>
  <a class="nav" style="left:595px" href="#">HOME</a>
  <a class="nav" style="left:739px" href="#">BUY ADDONS</a>
  <a class="btn btn-login" href="#">LOGIN</a>
</header>

<section class="hero" role="img" aria-label="Photo of a hand pressing a panic button mounted under a desk edge">
  <h1 class="hero-title">FEEL CONFIDENT THAT<br>YOUR STAFF IS <span class="accent">PROTECTED</span></h1>
  <p class="hero-sub">GET A REVOLUTIONARY NEW ELECTRONIC PANIC BUTTON</p>
  <a class="btn btn-hero" href="#">GET STARTED</a>
</section>

<div class="features">
  <div class="feature" style="left:0">
    <svg width="72" height="78" viewBox="0 0 72 78" fill="none" stroke="#3a8fd6" stroke-width="2.4" stroke-linecap="round">
      <circle cx="38" cy="24" r="12"/><path d="M33 36v8h10v-8M35 48h6"/>
      <path d="M38 4v4M22 10l3 3M54 10l-3 3M18 24h4M54 24h4"/>
      <path d="M6 60c8-6 14-6 22 0h14c4 0 4 6 0 6H28M6 72c10-2 30 2 40-6l16-12c3-2 6 2 3 5L48 74"/>
    </svg>
    <p>Problems Stopped Before They Start<br>For Any Type Of Organization</p>
  </div>
  <div class="feature" style="left:295px">
    <svg width="72" height="78" viewBox="0 0 72 78" fill="none" stroke="#3a8fd6" stroke-width="2.4" stroke-linecap="round">
      <path d="M36 10v58M46 22c-4-6-22-6-22 4s22 6 22 18-20 10-24 4"/>
      <path d="M42 8h20v10H44M6 58h20v10H8M58 30l6-4M58 38h8M10 40H4M10 48l-6 4"/>
    </svg>
    <p>Affordable Prices Starting at $18 per month.<br>No Contracts. No Hidden Costs.</p>
  </div>
  <div class="feature" style="left:600px">
    <svg width="78" height="78" viewBox="0 0 78 78" fill="none" stroke="#3a8fd6" stroke-width="3" stroke-linejoin="round" stroke-linecap="round">
      <path d="M39 8L74 68H4Z"/><path d="M39 30v20M39 58v2"/>
    </svg>
    <p>Alerts by computer, mobile device,<br>text, phone, email, monitoring and E911</p>
  </div>
</div>

<section class="band problem" role="img" aria-label="Photo of a desk telephone beside a window">
  <h2 class="band-title" style="margin-top:55px">YOUR EMPOYEES SHOULDN'T<br>FEEL ALONE WHEN THEY NEED <span class="accent">HELP</span></h2>
  <p class="band-sub" style="margin-top:22px">DOES THIS PROBLEM MAKE YOU FEEL FRUSTRATED AND ANXIOUS?<br>PUT A SIMPLE SOLUTION IN THEIR HANDS</p>
  <a class="btn" href="#" style="position:absolute;left:495px;top:258px;width:210px;height:50px;font-size:17px">LEARN MORE</a>
</section>

<h2 class="section-title" style="top:1205px">WHY CHOOSE US</h2>
<div class="why" style="left:145px">
  <svg width="60" height="80" viewBox="0 0 60 80" fill="none" stroke="#3a8fd6" stroke-width="2.4" stroke-linecap="round" stroke-linejoin="round">
    <path d="M24 44V14a5 5 0 0110 0v24M34 34a5 5 0 0110 0v6M44 38a5 5 0 0110 0v14c0 14-8 22-20 22h-6C18 74 8 62 6 52l-2-8a5 5 0 019-3l11 10"/>
    <path d="M18 16a11 11 0 0122 0M12 16a17 17 0 0134 0"/>
  </svg>
  <h3>EASY TO USE</h3>
  <p>Press a button and let the right people know<br>you need help and open a chat window<br>letting everyone talk on resolving their<br>problem.</p>
</div>
<div class="why" style="left:453px;width:290px">
  <svg width="80" height="80" viewBox="0 0 80 80" fill="none" stroke="#3a8fd6" stroke-width="2.2" stroke-linecap="round" stroke-linejoin="round">
    <rect x="4" y="4" width="18" height="24" rx="2"/><rect x="56" y="4" width="22" height="16" rx="2"/>
    <path d="M26 46a10 10 0 0110-12 12 12 0 0122 4 8 8 0 010 16H28a8 8 0 01-2-8z"/>
    <rect x="4" y="58" width="22" height="16" rx="2"/><rect x="58" y="58" width="18" height="18" rx="2"/>
    <path d="M13 28v16h12M67 20v14M40 54v12H26M58 54v6"/>
  </svg>
  <h3>COMMUNICATE THE WAY YOU WANT</h3>
  <p style="margin-bottom:4px">We give you lots of options:</p>
  <div class="opts"><span>Computer</span><span style="text-align:center">Text</span><span>Mobile</span><span style="text-align:center">E911</span><span>Email</span><span style="text-align:center">Call Center</span><span>Phone call</span></div>
</div>
<div class="why" style="left:818px">
  <svg width="60" height="80" viewBox="0 0 60 80" fill="none" stroke="#3a8fd6" stroke-width="2.4" stroke-linecap="round" stroke-linejoin="round">
    <path d="M30 4l26 10v20c0 20-12 32-26 40C16 66 4 54 4 34V14Z"/><path d="M18 38l9 9 16-16"/>
  </svg>
  <h3>COST EFFECTIVE PROTECTION</h3>
  <p>By leveraging your existing network and<br>equipment we can lower your costs to give<br>better options to your staff.</p>
</div>

<section class="band earth" role="img" aria-label="Night view of Earth from orbit with city lights">
  <h2 class="band-title" style="margin-top:62px">WE KNOW HOW SCARY IT CAN FEEL TO<br>WORRY ABOUT EMPLOYEE <span class="accent">SAFETY</span></h2>
  <p class="band-sub" style="margin-top:20px">THAT'S WHY WE HAVE PROVIDED A WAY FOR<br>CUSTOMERS TO GET HELP TO STAFF EFFECTIVELY IN</p>
  <p class="stats" style="margin-top:20px"><span class="accent">45</span> STATES<span class="small">COVERING</span><span class="accent">5</span> COUNTRIES</p>
  <svg class="abs" style="left:564px;top:316px" width="72" height="72" viewBox="0 0 72 72" fill="none" stroke="#3a8fd6" stroke-width="2.5">
    <circle cx="36" cy="36" r="33"/><path d="M28 22l22 14-22 14Z" stroke-linejoin="round"/>
  </svg>
  <a class="btn" href="#" style="position:absolute;left:495px;top:423px;width:210px;height:52px;font-size:17px">WATCH MY DEMO</a>
</section>

<h2 class="section-title" style="top:2195px">SIMPLE START PLAN</h2>

<div class="plan-text" style="left:242px;top:2350px">
  <h3>EXPLORE YOUR CHOICES</h3>
  <ul><li>• PRICING</li><li>• TRIAL</li><li>• QUOTE</li><li>• HARDWARE</li></ul>
</div>
<div class="plan-img" role="img" aria-label="Photo of a staff member's navy shirt with a panic button worn on a lanyard" style="left:630px;top:2287px;width:330px;height:327px;background:linear-gradient(90deg,#d9dadc 0%,#232b3a 18%,#1c2230 80%,#cfd0d2 100%)"></div>

<div class="plan-img" role="img" aria-label="Photo of a hand placing a panic button into a jeans pocket" style="left:305px;top:2614px;width:380px;height:316px;background:linear-gradient(110deg,#2f4468 0%,#3d5680 45%,#8d97a6 75%,#e4e5e7 100%)"></div>
<div class="plan-text" style="left:752px;top:2672px">
  <h3>GET SETUP</h3>
  <ul><li>• INPUT YOUR ALERTS</li><li>• INPUT YOUR STAFF</li><li>• INSTALL OUR SOFTWARE</li></ul>
</div>

<div class="plan-text" style="left:165px;top:3010px;width:400px;text-align:center">
  <h3 style="font-size:20px;line-height:27px">FEEL CONFIDENT YOUR STAFF IS<br>PROTECTED</h3>
  <p style="font-size:14px;font-weight:700;color:var(--blue);line-height:30px">HIGH FIVE. YOU JUST TOO A MAJOR STEP TO GETTING<br>RID OF THE ANXIETY AND FRUSTRATION THIS GAVE<br>YOU.</p>
</div>
<div class="plan-img" role="img" aria-label="Photo of a panic button on a lanyard hanging on a wall beside a sticky note" style="left:600px;top:2930px;width:360px;height:305px;background:linear-gradient(90deg,#eeeeec 0%,#bdbcb6 40%,#8e8d88 70%,#a9a8a3 100%)"></div>

<a class="btn" href="#" style="position:absolute;left:495px;top:3283px;width:210px;height:52px;font-size:17px">WATCH MY DEMO</a>

<footer class="site-footer">
  <div class="foot-brand">
    <div class="brand-dot"></div>
    <div class="brand-name">CrewBeacon</div>
  </div>
  <p class="foot-about">When employees feel alone during a threatening situation, we give them a way to let the right resources know that they need help so you can feel confident that your staff is protected.</p>
  <div class="call">
    <svg width="54" height="54" viewBox="0 0 54 54" fill="none" stroke="#fff" stroke-width="2" stroke-linejoin="round" stroke-linecap="round">
      <path d="M8 6l10 2 4 10-6 4c3 7 8 12 15 15l4-6 10 4 2 10c-2 4-6 6-10 5C20 46 8 34 4 16 3 12 4 8 8 6z"/>
      <path d="M32 6a16 16 0 0116 16M32 13a9 9 0 019 9"/>
    </svg>
    <div><div class="call-label">CALL US</div><div class="call-num">1 – 800 – 555 – 0148</div></div>
  </div>
  <div class="foot-col" style="left:516px">
    <h4>SHOP</h4>
    <ul><li>ADD ONS</li><li>START MY DEMO</li><li>CUSTOM QUOTE</li><li>START TRIAL</li></ul>
  </div>
  <div class="foot-col" style="left:708px">
    <h4>ABOUT</h4>
    <ul><li>AFFILIATES</li><li>CONTACT</li><li>SUPPORT</li><li>EXISTING CUSTOMERS</li><li>INDUSTRIES</li><li>BLOG</li><li>FAQ</li></ul>
  </div>
  <div class="foot-col" style="left:932px">
    <h4>LEGAL</h4>
    <ul><li>PRIVACY POLICY</li><li>TERMS OF USE</li><li>END USER LICENSE</li><li>AGREEMENT</li></ul>
  </div>
  <div class="foot-rule"></div>
  <p class="copyright">©CrewBeacon 2020. ALL RIGHTS RESERVED.</p>
</footer>

</body>
</html>
```